Software Company Business Card

We are looking for a new design of our business card. The design will also be used in the rest of our branding and marketing materials as we want to keep it all uniform. We sell POS software to fine/luxury jewelers and also offer other business services as well to help the jeweler manage their business and need something more updated, technical and fresh, preferably more on the masculine side. We do not want any designs with gems in them but if possible would like to incorporate the circle and arrow in the logo into the design, but not a requirement if you can't make it work. I would like to see a variety of the mix. The colors need to remain our blue and orange and the logo can not change. The squiggly lines have been used as our corporate identity for over 20 years and its time to update. Our company name is PELK (Bright Ledger Counter Solutions).

Target Market(s)

High End Jewelers

Industry/Entity Type

Software

Contact Information for Business Card

Requirements
Must have
• Our logo and the colors must remain the same. Blue is #d95d39 and Orange is #0f5682.
Nice to have
• The circle and arrow incorporated but not a requirement.
Should not have
• Anything jewelry or gem related.

```html
<!DOCTYPE html>
<html lang="en">
<head>
<meta charset="utf-8">
<title>PELK Business Card</title>
<link href="https://fonts.googleapis.com/css2?family=Open+Sans:wght@400;600;700;800&display=swap" rel="stylesheet">
<style>
  :root {
    --brand-blue: #14537e;
    --brand-orange: #d35a36;
    --card-white: #f4f4f4;
    --ink: #222222;
    --stage: #e3e3e3;
    --badge-gold: #c9a24a;
    --badge-teal: #5f9c92;
    --badge-grey: #6b6b6b;
  }
  * { margin: 0; padding: 0; box-sizing: border-box; }
  html, body {
    width: 1200px; height: 960px; overflow: hidden;
    background: var(--stage);
    font-family: "Open Sans", Arial, sans-serif;
  }
  .canvas { position: relative; width: 1200px; height: 960px; }

  .card { position: absolute; left: 305px; width: 596px; height: 340px; overflow: hidden; }

  /* Front */
  .card-front { top: 120px; background: var(--brand-blue); }
  .card-front .wordmark {
    position: absolute; left: 325px; top: 235px;
    font-weight: 800; font-size: 64px; line-height: 1; letter-spacing: 0;
    color: #ffffff;
  }
  .card-front .tagline {
    position: absolute; left: 328px; top: 296px;
    font-weight: 700; font-size: 10.5px; line-height: 14px; color: #ffffff;
  }

  /* Back */
  .card-back { top: 513px; background: var(--card-white); }
  .card-back .wordmark {
    position: absolute; left: 42px; top: 31px;
    font-weight: 800; font-size: 58px; line-height: 1; letter-spacing: 0;
    color: var(--brand-blue);
  }
  .card-back .tagline {
    position: absolute; left: 45px; top: 89px;
    font-weight: 700; font-size: 10px; line-height: 13px; color: var(--brand-orange);
  }
  .logo-dot {
    position: absolute; left: 283px; top: 37px;
    width: 64px; height: 64px; border-radius: 50%;
    background: var(--brand-orange);
  }

  .person { position: absolute; left: 42px; top: 156px; }
  .person-name { font-weight: 600; font-size: 20px; color: var(--brand-blue); line-height: 1.2; }
  .person-title { font-size: 15.5px; color: var(--ink); line-height: 1.4; }

  .contacts { position: absolute; left: 41px; top: 230px; list-style: none; }
  .contacts li {
    display: flex; align-items: center; gap: 4px;
    font-size: 15.5px; color: var(--ink); line-height: 20px;
  }
  .contacts svg { width: 15px; height: 13px; flex: none; }

  .partner-badge { position: absolute; left: 385px; }
  .badge-show { top: 152px; width: 172px; height: 58px; }
  .badge-society { top: 216px; width: 172px; height: 44px; }

  .web-tab {
    position: absolute; right: 0; top: 275px; width: 224px; height: 25px;
    background: var(--brand-orange);
    clip-path: polygon(14px 0, 100% 0, 100% 100%, 0 100%);
    color: #ffffff; font-size: 15.5px; line-height: 25px;
    padding-left: 36px;
  }
  .rule-orange {
    position: absolute; left: 0; right: 0; top: 300px; height: 4px;
    background: var(--brand-orange);
  }
  .address-bar {
    position: absolute; left: 0; right: 0; top: 306px; height: 34px;
    background: var(--brand-blue);
    color: #ffffff; font-size: 15.5px; line-height: 34px; padding-left: 42px;
  }
</style>
</head>
<body>
<main class="canvas">

  <section class="card card-front" aria-label="Card front">
    <div class="wordmark">PELK</div>
    <div class="tagline">BUSINESS &amp; TECHNOLOGY SOLUTIONS</div>
  </section>

  <section class="card card-back" aria-label="Card back">
    <div class="wordmark">PELK</div>
    <div class="logo-dot"></div>
    <div class="tagline">BUSINESS &amp; TECHNOLOGY SOLUTIONS</div>

    <div class="person">
      <p class="person-name">Declan Whitford</p>
      <p class="person-title">Director of Global Operations</p>
    </div>

    <ul class="contacts">
      <li>
        <svg viewBox="0 0 16 14" aria-hidden="true"><path d="M3 1l3 3-2 2c1 2 2.5 3.5 4.5 4.5l2-2 3 3-2 2C6 13 2 8.5 1 3z" fill="var(--brand-orange)"/></svg>
        +1 800 555-0142
      </li>
      <li>
        <svg viewBox="0 0 16 14" aria-hidden="true"><rect x="4" y="1" width="8" height="4" fill="none" stroke="var(--brand-orange)" stroke-width="1.5"/><rect x="1" y="5" width="14" height="6" rx="1" fill="var(--brand-orange)"/><rect x="4" y="9" width="8" height="4" fill="#fff" stroke="var(--brand-orange)" stroke-width="1.2"/></svg>
        +1 702 555-0187
      </li>
      <li>
        <svg viewBox="0 0 16 14" aria-hidden="true"><rect x="1" y="2" width="14" height="10" fill="none" stroke="var(--brand-orange)" stroke-width="1.5"/><path d="M1 2l7 6 7-6" fill="none" stroke="var(--brand-orange)" stroke-width="1.5"/></svg>
        declan@pelkusa.com
      </li>
    </ul>

    <svg class="partner-badge badge-show" viewBox="0 0 172 58" role="img" aria-label="Partner trade show badge">
      <rect x="0" y="0" width="172" height="58" rx="4" fill="var(--badge-gold)"/>
    </svg>
    <svg class="partner-badge badge-society" viewBox="0 0 172 44" role="img" aria-label="Partner society membership badge">
      <rect x="1" y="1" width="170" height="42" rx="4" fill="none" stroke="var(--badge-teal)" stroke-width="2"/>
      <line x1="12" y1="34" x2="160" y2="34" stroke="var(--badge-grey)" stroke-width="1"/>
    </svg>

    <div class="web-tab">www.pelkusa.com</div>
    <div class="rule-orange"></div>
    <div class="address-bar">1480 Meridian Park Drive, Suite 210, Henderson, NV 89052</div>
  </section>

</main>
</body>
</html>
```